Site Redesign in WORDPRESS for a Aerial Survey Company

We are looking for an updated look to our website that reflects our aerial drone services. Our company is changing directions from helping to provide legal documentation for companies to operate UAVs for commercial operations, to now providing Aerial Data Collection services. We need the new website to focus on this new direction.

Wordpress Design (Uncoded - PSD layout only)

Current site: http://vantorimaging.com/
Business card attached

VISUAL
********
The new pages should be visually top-notch, appealing, and more user-friendly to navigate, and represent our professionalism and level of expertise. We love the use of images, both great photography and technical. Our specialty is the use of Aerial LiDAR.

Our current site uses the Bramble template.

Colors: I've attached the Pantone for our logo colors

Fonts: Simple, clean and professional. We are not worried about specific fonts so long as they tie or compliment our logo.

STRUCTURE
****************
In the attached document I have laid out the pages we would like to have and the content outline of the content these pages will include.

We're happy to answer you questions in the comments and to provide quick feedback and additional info if necessary.

Target Market(s)

Agricultural and Engineering firms

Industry/Entity Type

Agribusiness

Coding

Coded - Design and coding required

Number of Pages Required

5+ page

Font styles to use
Sans Serif

Colors
0392cd
9bcb3c
ffffff

Requirements
Must have
• We need at a minimum a design with the Home/Landing, Services, and about. Need to be able to adapt the site as we add new services and increase our partnerships.
• Please provide in WordPress format.
• Links to social media: Friendlink, Chirper, Instagram
Nice to have
• We like parrallax, but in the end it's about the overall feel of the site.
Should not have
• Please, professional designs only.

```html
<!DOCTYPE html>
<html lang="en">
<head>
<meta charset="utf-8">
<title>Corrimar Aerial – Aerial Data Collection</title>
<link rel="stylesheet" href="https://fonts.googleapis.com/css2?family=Oswald:wght@400;500&family=Lato:wght@400;700&family=Open+Sans:wght@400;600&display=swap">
<style>
:root{
  --blue:#0392cd;
  --green:#6cab3c;
  --lime:#9bcb3c;
  --dark:#2a2a2a;
  --nav:#262626;
  --ink:#1e1e1e;
  --text:#333;
  --light:#efefef;
  --band:#e2e2e2;
  --white:#fff;
  --foot:#141414;
}
*{box-sizing:border-box;margin:0;padding:0}
html,body{width:1200px;height:2651px;overflow:hidden}
body{position:relative;background:var(--white);font-family:'Lato',sans-serif;color:var(--text)}
section,header,nav,footer{position:absolute;left:0;width:1200px}
.abs{position:absolute}
.heading{font-family:'Oswald',sans-serif;font-weight:400;font-size:30px;color:var(--ink);text-transform:uppercase;text-align:center}
.heading span{color:var(--blue)}
.rule{position:absolute;height:1px;background:#bbb}
.rule::after{content:"";position:absolute;left:50%;top:-1px;width:120px;height:3px;margin-left:-60px;background:var(--blue)}

/* header */
.site-header{top:0;height:92px;background:var(--white)}
.brand{left:131px;top:18px;display:flex;align-items:center;gap:12px}
.brand-mark{width:52px;height:52px;background:var(--blue);border-radius:4px}
.brand-name{font-family:'Oswald',sans-serif;font-weight:500;font-size:30px;color:var(--blue);text-transform:uppercase;line-height:1}
.brand-tag{font-family:'Lato',sans-serif;font-size:11px;color:var(--blue);margin-top:3px}
.top-social{right:130px;top:10px;display:flex;gap:10px}
.top-social i{display:block;width:30px;height:30px;border-radius:50%;background:var(--green)}
.top-contact{right:130px;top:50px;display:flex;gap:30px;font-family:'Oswald',sans-serif;font-size:15px;color:var(--ink)}
.top-contact span{display:flex;align-items:center;gap:8px}

/* nav */
.main-nav{top:92px;height:49px;background:var(--nav)}
.main-nav ul{list-style:none;display:flex;position:absolute;left:131px;height:49px}
.main-nav li{height:49px;padding:0 24px;display:flex;align-items:center;font-family:'Oswald',sans-serif;font-size:15px;color:var(--white);text-transform:uppercase;border-right:1px solid #444}
.main-nav li.active{background:var(--green)}

/* hero */
.hero{top:141px;height:469px;background:linear-gradient(180deg,#f1f3f3 0%,#dfe4e1 38%,#5d7a2e 44%,#6f8f34 70%,#557528 100%)}
.hero-caption{left:0;bottom:0;width:1200px;height:62px;background:rgba(0,0,0,.45);font-family:'Oswald',sans-serif;font-size:30px;color:var(--white);text-align:center;line-height:62px}
.hero-arrow{top:222px;width:44px;height:44px;background:rgba(40,40,40,.8)}
.hero-arrow.prev{left:0}.hero-arrow.next{right:0}

/* welcome */
.welcome{top:610px;height:353px}
.welcome .heading{position:absolute;top:28px;width:100%}
.welcome p{position:absolute;left:131px;top:115px;width:648px;font-size:16px;line-height:26px;color:#222}
.btn{background:var(--blue);color:var(--white);font-family:'Lato',sans-serif;font-weight:700;border-radius:4px;text-align:center}
.welcome .btn{left:131px;top:265px;width:92px;height:32px;line-height:32px;font-size:13px}
.video{left:809px;top:118px;width:257px;height:194px;border:4px solid #222;background:linear-gradient(160deg,#b9c9dc,#5b6f88 60%,#3a3f46)}
.video-bar{left:0;bottom:0;width:100%;height:24px;background:#111}
.video-play{left:106px;top:74px;width:44px;height:32px;border-radius:8px;background:#e52d27}

/* services */
.services{top:963px;height:332px;background:var(--light)}
.services .heading{position:absolute;top:26px;width:100%}
.service{position:absolute;top:120px;width:190px;margin-left:-95px;text-align:center}
.ring{width:120px;height:120px;margin:0 auto;border-radius:50%;border:7px solid var(--blue);background:#222;display:flex;align-items:center;justify-content:center}
.service.active .ring{background:var(--green)}
.service h3{margin-top:26px;font-family:'Open Sans',sans-serif;font-weight:600;font-size:13px;line-height:18px;color:#222;text-transform:uppercase}

/* news + capabilities */
.columns{top:1295px;height:393px}
.col-title{position:absolute;top:26px;font-family:'Oswald',sans-serif;font-weight:400;font-size:28px;text-transform:uppercase;color:var(--ink)}
.col-title span{color:var(--blue)}
.col-line{position:absolute;top:69px;height:1px;background:#ccc}
.col-line::after{content:"";position:absolute;left:0;top:0;border:10px solid transparent;border-top-color:var(--blue);border-width:9px 12px 0 12px}
.pager{left:545px;top:34px;font-family:'Oswald',sans-serif;font-size:20px;color:#222}
.news{position:absolute;left:131px;width:441px;height:116px}
.news-thumb{left:0;top:0;width:131px;height:116px;background:linear-gradient(140deg,#3c5b7a,#b78a3f 55%,#2a2a2a)}
.news-body{left:152px;top:0;width:289px}
.news h4{font-family:'Lato',sans-serif;font-weight:700;font-size:14px;color:#222}
.news time{display:block;font-family:'Oswald',sans-serif;font-size:14px;color:var(--green);margin:3px 0 4px}
.news p{font-size:12.5px;line-height:18px;color:#444}
.news a{font-size:12.5px;color:#222;text-decoration:none}
.capability{position:absolute;left:622px;width:446px;height:124px;border:5px solid #777;background:linear-gradient(180deg,#3a4a5d,#1f2f44);text-align:center;color:var(--white)}
.capability h4{font-family:'Oswald',sans-serif;font-weight:400;font-size:21px;margin-top:22px;text-transform:uppercase}
.capability p{font-size:12.5px;line-height:18px;margin:8px auto 0;width:360px}

/* partners */
.partners{left:131px;top:1714px;width:937px;height:97px;border:1px solid #ddd;background:#f7f7f7}
.partners-label{left:0;top:0;width:161px;height:97px;background:var(--blue);color:var(--white);font-family:'Oswald',sans-serif;font-size:20px;line-height:28px;padding:20px 0 0 24px;text-transform:uppercase}
.partners-label::after{content:"";position:absolute;right:-12px;top:36px;border-left:12px solid var(--blue);border-top:12px solid transparent;border-bottom:12px solid transparent}
.partner-list{left:200px;top:0;height:97px;display:flex;align-items:center;gap:50px;font-family:'Oswald',sans-serif;font-size:32px;color:#666}
.partner-list span{display:flex;align-items:center;gap:10px}
.partner-list i{width:22px;height:22px;border-radius:50%;background:#777;display:block}

/* newsletter */
.newsletter{top:1859px;height:284px;background:var(--band)}
.newsletter .heading{position:absolute;top:34px;width:100%}
.newsletter p{position:absolute;left:150px;top:118px;width:900px;text-align:center;font-size:16px;line-height:28px;color:#222}
.field{background:var(--white);font-size:14px;color:#333;padding-left:14px;display:flex;align-items:center}
.newsletter .field{left:270px;top:194px;width:465px;height:44px}
.newsletter .btn{left:747px;top:194px;width:184px;height:44px;line-height:44px;font-size:16px;border-radius:0;text-transform:uppercase;padding-right:40px}
.btn-arrow{position:absolute;right:0;top:0;width:44px;height:100%;background:rgba(255,255,255,.15)}

/* contact */
.contact{top:2143px;height:451px;background:var(--dark);color:var(--white)}
.contact .heading{position:absolute;top:30px;width:100%;color:var(--white)}
.form-field{left:131px;width:270px;height:37px;background:var(--white);color:#444;font-size:13px;padding:9px 12px}
.contact .submit{left:131px;top:373px;width:150px;height:39px;line-height:39px;font-size:16px;border-radius:0;text-transform:uppercase;text-align:left;padding-left:18px}
.address{left:424px;top:158px;width:200px;font-size:14px;line-height:21px;color:#eee}
.address .row{display:flex;gap:12px;margin-bottom:28px}
.address b{font-weight:700;text-transform:uppercase;font-size:13.5px}
.map{left:643px;top:149px;width:276px;height:238px;border:4px solid var(--lime);background:linear-gradient(135deg,#d9dfcf,#b9cfe6 55%,#e9e3cf)}
.social-list{left:944px;top:154px}
.social-list .item{display:flex;align-items:center;gap:18px;height:65px;font-family:'Open Sans',sans-serif;font-size:12px;text-transform:uppercase;color:#eee}
.social-list i{display:block;width:40px;height:40px;border-radius:50%;background:var(--blue);border:3px solid #1f5f86}
.social-list .rss i{background:#f07c1d;border-color:#9c4d0d}
.site-footer{top:2594px;height:57px;background:var(--foot);color:#ddd;font-family:'Open Sans',sans-serif;font-size:13px;text-align:center;line-height:57px}
</style>
</head>
<body>

<header class="site-header">
  <div class="abs brand">
    <div class="brand-mark"></div>
    <div>
      <div class="brand-name">Corrimar Aerial</div>
      <div class="brand-tag">Proven Leaders. Expert Solutions.</div>
    </div>
  </div>
  <div class="abs top-social"><i></i><i></i><i></i><i></i></div>
  <div class="abs top-contact">
    <span><svg width="14" height="14" viewBox="0 0 24 24"><path fill="#6cab3c" d="M6.6 10.8a15 15 0 006.6 6.6l2.2-2.2c.3-.3.7-.4 1-.2 1.1.4 2.3.6 3.6.6.6 0 1 .4 1 1V20c0 .6-.4 1-1 1A17 17 0 013 4c0-.6.4-1 1-1h3.5c.6 0 1 .4 1 1 0 1.3.2 2.5.6 3.6.1.3 0 .7-.2 1z"/></svg>123-456-7890</span>
    <span><svg width="16" height="12" viewBox="0 0 16 12"><rect width="16" height="12" fill="#6cab3c"/><path d="M0 0l8 6 8-6" stroke="#fff" fill="none"/></svg>dpell@corrimaraerial.com</span>
  </div>
</header>

<nav class="main-nav">
  <ul>
    <li class="active">Home</li><li>Services</li><li>Capabilities</li><li>About Us</li><li>Partners</li><li>Blog &amp; Upcoming Events</li><li>Contact Us</li>
  </ul>
</nav>

<section class="hero" role="img" aria-label="Operator flying a camera drone over a green farm field">
  <div class="abs hero-arrow prev"><svg width="44" height="44"><path d="M26 14l-8 8 8 8" stroke="#fff" stroke-width="3" fill="none"/></svg></div>
  <div class="abs hero-arrow next"><svg width="44" height="44"><path d="M18 14l8 8-8 8" stroke="#fff" stroke-width="3" fill="none"/></svg></div>
  <div class="abs hero-caption">We Provide Aerial Data Collection Service For Agricultural And Engineering Firms</div>
</section>

<section class="welcome">
  <h2 class="heading">Welcome to <span>Corrimar Aerial</span></h2>
  <div class="rule" style="left:306px;top:84px;width:588px"></div>
  <p>Lorem ipsum dolor sit amet, consectetuer adipiscing elit, sed diam nonummy nibh euismod tincidunt ut laoreet dolore magna aliquam erat volutpat. Ut wisi enim ad minim veniam, quis nostrud exerci tation ullamcorper suscipit lobortis nisl ut aliquip ex ea commodo consequat. Duis autem vel eum iriure dolor.&nbsp; putate velit esse molestie consequat,&nbsp; duis dolore te feugait nulla facilisi.</p>
  <div class="abs btn">Read More</div>
  <div class="abs video" role="img" aria-label="Video of an inspection drone flying beside a steel tower">
    <div class="abs video-play"><svg width="44" height="32"><path d="M17 9l11 7-11 7z" fill="#fff"/></svg></div>
    <div class="abs video-bar"><svg width="249" height="24"><rect x="8" y="7" width="3" height="10" fill="#fff"/><rect x="14" y="7" width="3" height="10" fill="#fff"/><rect x="26" y="11" width="120" height="3" fill="#0392cd"/><rect x="146" y="11" width="30" height="3" fill="#666"/><circle cx="222" cy="12" r="6" fill="#ddd"/></svg></div>
  </div>
</section>

<section class="services">
  <h2 class="heading">Our <span>Services</span></h2>
  <div class="rule" style="left:506px;top:79px;width:188px;background:transparent"></div>
  <div class="service active" style="left:191px"><div class="ring"><svg width="50" height="60" viewBox="0 0 50 60" fill="#fff"><rect x="23" y="8" width="4" height="50"/><ellipse cx="17" cy="20" rx="5" ry="9"/><ellipse cx="33" cy="20" rx="5" ry="9"/><ellipse cx="17" cy="34" rx="5" ry="9"/><ellipse cx="33" cy="34" rx="5" ry="9"/><ellipse cx="25" cy="7" rx="4" ry="8"/></svg></div><h3>Precision<br>Agriculture</h3></div>
  <div class="service" style="left:348px"><div class="ring"><svg width="60" height="50" viewBox="0 0 60 50" fill="#fff"><rect x="4" y="44" width="52" height="5"/><path d="M10 44l10-28 10 28h-4l-6-18-6 18z"/><rect x="14" y="10" width="36" height="6" transform="rotate(-12 32 13)"/><rect x="44" y="20" width="4" height="24"/></svg></div><h3>Exploration, Oil,<br>Gas, &amp; Mineral</h3></div>
  <div class="service" style="left:505px"><div class="ring"><svg width="56" height="44" viewBox="0 0 56 44" fill="#fff"><path d="M4 10h12l4-6h16l4 6h12v32H4z"/><circle cx="28" cy="25" r="10" fill="#222"/><circle cx="28" cy="25" r="6"/></svg></div><h3>Video &amp;<br>Still Images</h3></div>
  <div class="service" style="left:661px"><div class="ring"><svg width="40" height="60" viewBox="0 0 40 60" fill="#fff"><rect x="10" y="16" width="20" height="42" rx="5"/><rect x="16" y="8" width="8" height="8"/><path d="M24 10h10l2 6" stroke="#fff" stroke-width="3" fill="none"/></svg></div><h3>Public<br>Services</h3></div>
  <div class="service" style="left:836px"><div class="ring"><svg width="44" height="56" viewBox="0 0 44 56" fill="#fff"><path d="M4 10h36v46H4z"/><g fill="#222"><rect x="10" y="16" width="6" height="6"/><rect x="19" y="16" width="6" height="6"/><rect x="28" y="16" width="6" height="6"/><rect x="10" y="27" width="6" height="6"/><rect x="19" y="27" width="6" height="6"/><rect x="28" y="27" width="6" height="6"/><rect x="18" y="42" width="8" height="14"/></g></svg></div><h3>Commercial &amp;<br>Industrial Inspections</h3></div>
  <div class="service" style="left:1007px"><div class="ring"><svg width="56" height="48" viewBox="0 0 56 48" fill="none" stroke="#fff" stroke-width="3"><path d="M4 8l14-4 14 4 14-4v36l-14 4-14-4-14 4z"/><path d="M18 4v36M32 8v36"/><circle cx="44" cy="34" r="10" fill="#222"/></svg></div><h3>GIS &amp;<br>Mapping</h3></div>
</section>

<section class="columns">
  <h2 class="col-title" style="left:131px">Recent News / <span>Blog</span></h2>
  <div class="abs pager">&lsaquo; &rsaquo;</div>
  <div class="col-line" style="left:131px;width:441px"></div>
  <h2 class="col-title" style="left:622px">Our <span>Capabilities</span></h2>
  <div class="col-line" style="left:622px;width:446px"></div>

  <article class="news" style="top:101px">
    <div class="abs news-thumb" role="img" aria-label="Team assembling a drone"></div>
    <div class="abs news-body"><h4>Lorem Ipsum Dolor&nbsp; Consecte</h4><time>27 Jan 2016</time><p>Duis autem vel eum iriure dolor in hendreri immo vulputate velit esse molestie consequatn vel illum dolore eu feugiat nulla facilisis...</p><a>Read More</a></div>
  </article>
  <div class="abs" style="left:283px;top:234px;width:289px;height:1px;background:#ddd"></div>
  <article class="news" style="top:251px">
    <div class="abs news-thumb" role="img" aria-label="Engineers at a drone workshop"></div>
    <div class="abs news-body"><h4>Lorem Ipsum Dolor&nbsp; Consecte</h4><time>27 Jan 2016</time><p>Duis autem vel eum iriure dolor in hendreri immo vulputate velit esse molestie consequatn vel illum dolore eu feugiat nulla facilisis...</p><a>Read More</a></div>
  </article>

  <div class="capability" style="top:101px" role="img" aria-label="Drones flying against a dark sky"><h4>Drones</h4><p>Lorem ipsum dolor sit amet, consectetuer adipiscing elit, sed magna aliquam erat volutpat [+]</p></div>
  <div class="capability" style="top:241px" role="img" aria-label="Camera drone against a blue sky"><h4>Cameras</h4><p>Lorem ipsum dolor sit amet, consectetuer adipiscing elit, sed magna aliquam erat volutpat [+]</p></div>
</section>

<section class="partners">
  <div class="abs partners-label">Our Clients<br>or Partners</div>
  <div class="abs partner-list">
    <span><i></i>Heldwick</span><span>Tavrena</span><span>Quarne</span><span><i></i>Pellacor</span>
  </div>
</section>

<section class="newsletter">
  <h2 class="heading">Newsletter <span>Sign Up</span></h2>
  <div class="rule" style="left:424px;top:84px;width:352px"></div>
  <p>Lorem ipsum dolor sit amet, consectetuer adipiscing elit, sed diam nonummy nibh euismod tincidunt ut laoreet dolore magna aliquam erat volutpat. Ut wisi enim ad minim veniam.</p>
  <div class="abs field">Enter your email address</div>
  <div class="abs btn">Subscribe<span class="btn-arrow"><svg width="44" height="44"><path d="M19 16l6 6-6 6" stroke="#fff" stroke-width="2" fill="none"/></svg></span></div>
</section>

<section class="contact">
  <h2 class="heading">Contact Us</h2>
  <div class="rule" style="left:376px;top:84px;width:448px;background:#777"></div>
  <div class="abs form-field" style="top:147px">Name</div>
  <div class="abs form-field" style="top:195px">Email</div>
  <div class="abs form-field" style="top:242px">Phone</div>
  <div class="abs form-field" style="top:288px;height:68px">Message</div>
  <div class="abs btn submit">Submit<span class="btn-arrow"><svg width="44" height="39"><path d="M19 13l6 6-6 6" stroke="#fff" stroke-width="2" fill="none"/></svg></span></div>

  <div class="abs address">
    <div class="row"><svg width="12" height="16" viewBox="0 0 12 16"><path d="M6 0a6 6 0 00-6 6c0 4 6 10 6 10s6-6 6-10a6 6 0 00-6-6z" fill="#0392cd"/><circle cx="6" cy="6" r="2" fill="#2a2a2a"/></svg><div><b>Corrimar Aerial</b><br>123 euismod cidun uop laoreet laoreet dol magna</div></div>
    <div class="row"><svg width="14" height="14" viewBox="0 0 24 24"><path fill="#0392cd" d="M6.6 10.8a15 15 0 006.6 6.6l2.2-2.2c.3-.3.7-.4 1-.2 1.1.4 2.3.6 3.6.6.6 0 1 .4 1 1V20c0 .6-.4 1-1 1A17 17 0 013 4c0-.6.4-1 1-1h3.5c.6 0 1 .4 1 1 0 1.3.2 2.5.6 3.6.1.3 0 .7-.2 1z"/></svg>123-456-7890</div>
    <div class="row"><svg width="14" height="14" viewBox="0 0 14 14"><rect x="3" y="0" width="8" height="4" fill="#0392cd"/><rect x="0" y="4" width="14" height="6" fill="#0392cd"/><rect x="3" y="9" width="8" height="5" fill="#0392cd"/></svg>123-456-7890</div>
    <div class="row"><svg width="14" height="11" viewBox="0 0 16 12"><rect width="16" height="12" fill="#0392cd"/><path d="M0 0l8 6 8-6" stroke="#2a2a2a" fill="none"/></svg>dpell@corrimaraerial.com</div>
  </div>

  <div class="abs map" role="img" aria-label="Street map showing the office location"></div>

  <div class="abs social-list">
    <div class="item"><i></i>Friendlink</div>
    <div class="item"><i></i>Chirper</div>
    <div class="item"><i></i>Proflink</div>
    <div class="item rss"><i></i>RSS Feed</div>
  </div>
</section>

<footer class="site-footer">Copyright © 2016 Corrimar Aerial. All Rights Reserved</footer>

</body>
</html>
```